Needed Box Packaging: Dog XL Puppy Pee/Poo Pads

We're looking for a creative and fun design for our XL puppy pads. Attached is all the documents you will need.

Our pads are unique with Bamboo Charcoal and optional Adhesive sticker backing on the corners. 23" x 35" is the size. There's 50 per box.

ABSORBS 2x as much, 2x as fast, so you never come home to ruined floors
BLACK puppy pads, so your pets mess stays discrete and you never see a yellow stain on a white puppy pad in your home
ODOR ELIMINATION with carbon technology for all-day use to ensure your home stays fresh
LEAK PROOF Tidewell Polymer turns liquid into gel instantly to guarantee dry floors and easy clean up
PHEROMONE ATTRACTION to ensure pets feel comfortable and knows to hit the right spot every time

Target Market(s)

Dog owners

Font styles to use
Sans Serif

Colors
33a6d7
33b8a4
acd036
fbee3d
faa54b

Requirements
Must have
• Must have logo, size of pads, benefits, UPC code, number packed per box, pictures of a dog and picture of the pads
Should not have
• cats

```html
<!DOCTYPE html>
<html lang="en">
<head>
<meta charset="utf-8">
<title>XL Puppy Training Pads – Box Sides 3 and 4</title>
<link rel="stylesheet" href="https://fonts.googleapis.com/css2?family=Roboto+Condensed:wght@300;700&family=Roboto+Slab:wght@700;800&family=Anton&display=swap">
<style>
  :root {
    --cream: #fefcd4;
    --ink: #111111;
    --charcoal: #3a3a3a;
    --white: #ffffff;
    --lime: #acd036;
    --amber: #f6a81e;
  }
  * { margin: 0; padding: 0; box-sizing: border-box; }
  html, body {
    width: 1200px;
    height: 1145px;
    overflow: hidden;
    background: var(--cream);
  }
  .sheet {
    position: relative;
    width: 1200px;
    height: 1145px;
  }
  .side-label {
    position: absolute;
    left: 146px;
    font-family: "Roboto Condensed", sans-serif;
    font-weight: 300;
    font-size: 80px;
    line-height: 1;
    color: var(--ink);
    letter-spacing: -1px;
  }
  .side-label--three { top: 88px; }
  .side-label--four { top: 628px; }
  .box-side {
    position: absolute;
    left: 146px;
    width: 898px;
    height: 314px;
    display: block;
  }
  .box-side--three { top: 201px; }
  .box-side--four { top: 741px; }
  .box-side--three .panel-fill { fill: var(--lime); }
  .box-side--four .panel-fill { fill: var(--amber); }
  .size-tag { font-family: "Roboto Slab", serif; font-weight: 800; font-size: 74px; fill: var(--charcoal); }
  .product-name { font-family: "Roboto Slab", serif; font-weight: 800; font-size: 104px; fill: var(--white); }
  .product-sub { font-family: "Roboto Slab", serif; font-weight: 700; font-size: 44px; fill: var(--white); }
  .count { font-family: "Anton", sans-serif; font-size: 186px; fill: var(--white); }
  .count-unit { font-family: "Roboto Slab", serif; font-weight: 700; font-size: 48px; fill: var(--white); }
  .pad-size { font-family: "Roboto Condensed", sans-serif; font-weight: 700; font-size: 44px; fill: var(--white); }
</style>
</head>
<body>
<main class="sheet">
  <h2 class="side-label side-label--three">SIDE 3</h2>
  <svg class="box-side box-side--three" viewBox="0 0 898 314" aria-label="Side 3: XL Puppy Training Pads, 50 pieces, 23 by 35 inches">
    <rect class="panel-fill" width="898" height="314"/>
    <text class="size-tag" x="54" y="95" textLength="100" lengthAdjust="spacingAndGlyphs">XL</text>
    <text class="product-name" x="54" y="185" textLength="360" lengthAdjust="spacingAndGlyphs">PUPPY</text>
    <text class="product-sub" x="54" y="231" textLength="218" lengthAdjust="spacingAndGlyphs">TRAINING</text>
    <text class="product-sub" x="54" y="273" textLength="112" lengthAdjust="spacingAndGlyphs">PADS</text>
    <text class="count" x="668" y="175" textLength="170" lengthAdjust="spacingAndGlyphs">50</text>
    <text class="count-unit" x="670" y="231" textLength="162" lengthAdjust="spacingAndGlyphs">PIECES</text>
    <text class="pad-size" x="668" y="273" textLength="166" lengthAdjust="spacingAndGlyphs">23” x 35”</text>
  </svg>

  <h2 class="side-label side-label--four">SIDE 4</h2>
  <svg class="box-side box-side--four" viewBox="0 0 898 314" aria-label="Side 4: XL Puppy Training Pads, 50 pieces, 23 by 35 inches">
    <rect class="panel-fill" width="898" height="314"/>
    <text class="size-tag" x="54" y="95" textLength="100" lengthAdjust="spacingAndGlyphs">XL</text>
    <text class="product-name" x="54" y="185" textLength="360" lengthAdjust="spacingAndGlyphs">PUPPY</text>
    <text class="product-sub" x="54" y="231" textLength="218" lengthAdjust="spacingAndGlyphs">TRAINING</text>
    <text class="product-sub" x="54" y="273" textLength="112" lengthAdjust="spacingAndGlyphs">PADS</text>
    <text class="count" x="668" y="175" textLength="170" lengthAdjust="spacingAndGlyphs">50</text>
    <text class="count-unit" x="670" y="231" textLength="162" lengthAdjust="spacingAndGlyphs">PIECES</text>
    <text class="pad-size" x="668" y="273" textLength="166" lengthAdjust="spacingAndGlyphs">23” x 35”</text>
  </svg>
</main>
</body>
</html>
```